Deck Construction Company Billboard Design needed

We are a deck company with a 10'x32' billboard to fill with an advertisement. I'd like this ad to be 75% photo, 25% color-filled background with white text over (space to be divided side-to-side with line of some sort). This billboard artwork must be clearly legible and simple. The information I need on the billboard is as follows:
Porch QT (company name)
porchqt.ca
Outdoor Living Spaces
613-284-7390
Attached is a copy of the logo and photos I'd like to use (please choose one photo per billboard design)

Target Market(s)

30-70 year old home owners

Industry/Entity Type

Deck Builder

Font styles to use
Other font styles liked:
• Calibri

Colors
0054AA
0677BA
7BADD7
CADEEF
E8F1F8

Requirements
Must have
• Clear, simple white text. Dark blue fill, red accent
Nice to have
• Layering of photo and text
Should not have
• Too much to read

```html
<!DOCTYPE html>
<html lang="en">
<head>
<meta charset="utf-8">
<title>Porch QT Billboard</title>
<link href="https://fonts.googleapis.com/css2?family=Montserrat:wght@600;700;800;900&display=swap" rel="stylesheet">
<style>
  :root {
    --page: #ffffff;
    --panel: #ffffff;
    --ink: #0d0d0d;
    --red: #a80a0a;
    --navy: #0e2a48;
    --white: #ffffff;
    --photo-light: #9cbfdf;
    --photo-dark: #6d7c86;
  }
  * { margin: 0; padding: 0; box-sizing: border-box; }
  html, body {
    width: 976px;
    height: 1200px;
    overflow: hidden;
    background: var(--page);
    font-family: "Montserrat", sans-serif;
  }
  .billboard {
    position: absolute;
    left: 38px;
    top: 460px;
    width: 900px;
    height: 281px;
    background: var(--panel);
    overflow: hidden;
    box-shadow: 0 8px 28px rgba(0, 0, 0, 0.35);
  }
  .deck-photo {
    position: absolute;
    left: 0;
    top: 0;
    width: 443px;
    height: 220px;
    background: linear-gradient(135deg, var(--photo-light) 0%, var(--photo-dark) 100%);
  }
  .headline {
    position: absolute;
    left: 443px;
    top: 0;
    width: 420px;
    height: 195px;
    display: flex;
    flex-direction: column;
    align-items: center;
    justify-content: center;
    padding-top: 4px;
    line-height: 1;
    white-space: nowrap;
  }
  .brand-name {
    font-weight: 700;
    font-size: 58px;
    color: var(--ink);
    letter-spacing: 0.5px;
  }
  .tagline-top {
    font-weight: 900;
    font-size: 44px;
    color: var(--red);
    margin-top: 4px;
  }
  .tagline-bottom {
    font-weight: 900;
    font-size: 44px;
    color: var(--navy);
    margin-top: 2px;
  }
  .web-band {
    position: absolute;
    left: 0;
    top: 220px;
    width: 380px;
    height: 61px;
    background: var(--navy);
    display: flex;
    align-items: center;
    padding-left: 50px;
    gap: 10px;
  }
  .phone-band {
    position: absolute;
    left: 0;
    top: 195px;
    width: 900px;
    height: 86px;
    background: var(--red);
    clip-path: polygon(369px 0, 900px 0, 900px 86px, 340px 86px);
  }
  .phone {
    position: absolute;
    left: 414px;
    top: 195px;
    height: 86px;
    display: flex;
    align-items: center;
    gap: 14px;
  }
  .contact-text {
    color: var(--white);
    font-weight: 800;
    line-height: 1;
    white-space: nowrap;
  }
  .web-band .contact-text { font-size: 38px; }
  .phone .contact-text { font-size: 50px; letter-spacing: 0.5px; }
  .icon { flex: none; }
</style>
</head>
<body>
  <main class="billboard">
    <div class="deck-photo" role="img" aria-label="Photo of a two-level backyard deck with railings, stairs and patio furniture"></div>

    <div class="headline">
      <h1 class="brand-name">PORCH QT</h1>
      <p class="tagline-top">OUTDOOR</p>
      <p class="tagline-bottom">LIVING SPACES</p>
    </div>

    <div class="web-band">
      <svg class="icon" width="26" height="26" viewBox="0 0 24 24" fill="none" stroke="#ffffff" stroke-width="1.8">
        <circle cx="12" cy="12" r="10.5"/>
        <ellipse cx="12" cy="12" rx="4.5" ry="10.5"/>
        <line x1="1.5" y1="12" x2="22.5" y2="12"/>
        <line x1="3.5" y1="6.5" x2="20.5" y2="6.5"/>
        <line x1="3.5" y1="17.5" x2="20.5" y2="17.5"/>
        <line x1="12" y1="1.5" x2="12" y2="22.5"/>
      </svg>
      <span class="contact-text">porchqt.ca</span>
    </div>

    <div class="phone-band"></div>
    <div class="phone">
      <svg class="icon" width="36" height="36" viewBox="0 0 24 24" fill="none" stroke="#ffffff" stroke-width="1.4" stroke-linejoin="round" stroke-linecap="round">
        <path d="M5.5 2.5l3 .5 1.5 4-2 1.5a11 11 0 0 0 7.5 7.5l1.5-2 4 1.5.5 3-2 2.5C11 21 3 13 3 4.5z"/>
        <path d="M14 2.5a7.5 7.5 0 0 1 7.5 7.5"/>
        <path d="M14 6a4 4 0 0 1 4 4"/>
      </svg>
      <span class="contact-text">613-284-7390</span>
    </div>
  </main>
</body>
</html>
```